Anzeigengestaltung für eine Hausarztpraxis
Zielgruppe
Wir sind eine Hausarztpraxis mit zwei Standorten und suchen eine Ärztin oder einen Arzt zur Anstellung in der klassischen Hausarzt Medizin am Standort Erlenbrunn
Aufgabenstellung
Bitte beachtet den Text im Anhang, der ist schon vorgegeben. (Anzeigentext)
Wir suchen ein ruhiges, hochwertiges Layout für eine Stellenanzeige einer Hausarztpraxis in einem historischen Gebäude.
Der Text steht im Vordergrund, das Design soll zurückhaltend, klar und wertig sein.
Bitte keine Icons, keine bunten Farben, keine verspielten Elemente.
Gerne viel Weissraum, klare Typografie, ruhige Anmutung.
Schrift: Garamond für den Fliesstext (bereits gewählt).
Das Layout soll sowohl als PDF wie auch online funktionieren.
Optional: ein sehr dezentes grafisches Element oder eine ruhige Bildanmutung (z. B. Struktur, Licht, Architekturdetail).

```html
<!DOCTYPE html>
<html lang="de">
<head>
<meta charset="utf-8">
<title>Stellenanzeige Hausarztpraxis Erlenbrunn</title>
<link rel="stylesheet" href="https://fonts.googleapis.com/css2?family=EB+Garamond:wght@400;600&family=Poppins:wght@500;600&family=Open+Sans:ital@1&display=swap">
<style>
  :root {
    --stage: #e6e6e6;
    --paper: #f7f7f7;
    --band: #eceeef;
    --header: #6f7e8e;
    --ink: #3a3f45;
    --ink-soft: #55595e;
    --white: #ffffff;
    --accent: #8cc63f;
    --accent-soft: #d6e6c0;
    --rule: #7a8694;
  }
  * { box-sizing: border-box; margin: 0; padding: 0; }
  html, body { width: 1200px; height: 800px; overflow: hidden; }
  body { background: var(--stage); font-family: "EB Garamond", Garamond, serif; color: var(--ink); }

  .flyer {
    position: absolute; left: 322px; top: 7px;
    width: 556px; height: 786px;
    background: var(--paper);
    box-shadow: 0 2px 10px rgba(0,0,0,.12);
    overflow: hidden;
  }

  .hero {
    position: relative; height: 240px;
    background: var(--header);
    color: var(--white);
    padding: 28px 0 0 50px;
  }
  .hero-photo {
    position: absolute; right: 0; top: 0; width: 320px; height: 240px;
    background:
      linear-gradient(90deg, var(--header) 0%, rgba(111,126,142,0) 45%),
      linear-gradient(180deg, #8d99a6 0%, #9aa3aa 45%, #7f8a93 70%, #6f7e8e 100%);
  }
  .brand {
    position: relative; display: flex; align-items: center; gap: 8px;
    font-family: "Poppins", sans-serif; font-weight: 500; font-size: 12px;
    color: var(--white); letter-spacing: .2px;
  }
  .brand-dot { width: 9px; height: 9px; border-radius: 50%; background: var(--white); }
  .headline {
    position: relative; margin-top: 38px;
    font-family: "Poppins", sans-serif; font-weight: 600;
    font-size: 20px; line-height: 1.32; letter-spacing: .2px;
  }
  .tagline {
    position: relative; margin-top: 16px;
    font-family: "Open Sans", sans-serif; font-style: italic; font-size: 11px;
    color: #e6eaee;
  }

  .intro { padding: 22px 60px 18px 60px; font-size: 10.5px; line-height: 1.55; color: var(--ink-soft); }
  .intro p + p { margin-top: 5px; }

  .facts { background: var(--band); padding: 20px 50px 22px 60px; }
  .facts-row { display: flex; gap: 28px; }
  .fact { flex: 1; }
  .fact.wide { margin-top: 20px; }
  .fact-title {
    position: relative; font-weight: 600; font-size: 14px; color: var(--ink);
    padding-left: 4px; margin-bottom: 5px;
  }
  .fact-title::before {
    content: ""; position: absolute; left: -10px; top: -2px;
    width: 22px; height: 22px; border-radius: 50%;
    background: var(--accent-soft);
  }
  .fact-title span { position: relative; }
  .fact p { font-size: 10.5px; line-height: 1.55; color: var(--ink-soft); padding-left: 4px; }

  .contact { display: flex; padding: 26px 50px 0 64px; font-size: 10.5px; line-height: 1.55; color: var(--ink-soft); }
  .contact-note { flex: 1; padding-right: 26px; }
  .contact-note strong { color: var(--ink); font-weight: 600; white-space: nowrap; }
  .contact-mail { margin-top: 5px; }
  .label { color: var(--accent); font-weight: 600; }
  .contact-address { border-left: 1px solid var(--rule); padding-left: 24px; width: 150px; font-style: normal; }
  .contact-address .org { color: var(--accent); font-weight: 600; }
</style>
</head>
<body>
  <article class="flyer">
    <header class="hero">
      <div class="hero-photo" role="img" aria-label="Historisches Praxisgebäude mit Rundbrunnen im Hof, in ruhigem Grau getönt"></div>
      <div class="brand"><span class="brand-dot"></span>Praxis Lindenhof</div>
      <h1 class="headline">Hausarztmedizin mit Tiefe –<br>dort, wo man noch echte<br>Grundversorgung lebt</h1>
      <p class="tagline">Ein Ort, der trägt. Ein Team, das bleibt. Eine Arbeit, die Wertschätzung hat.</p>
    </header>

    <section class="intro">
      <p>Manche Orte verändern die Art, wie man arbeitet. Unsere Praxis in Erlenbrunn ist so ein Ort.
      In einem historischen Gebäude gelegen, mit grosszügigem Ambiente, warmen Vertäfelungen und kunstvoller Wandbemalung, entstehen hier Behandlungsräume von Ruhe und Würde. Kein steriler Praxisalltag, sondern ein Ort, der Gespräche trägt und medizinische Arbeit unterstützt.</p>
      <p>Für diesen besonderen Ort suchen wir eine Hausärztin oder einen Hausarzt, die oder der nicht einfach einen Arbeitsplatz sucht, sondern einen Platz, an dem Medizin menschlich sein darf.</p>
    </section>

    <section class="facts">
      <div class="facts-row">
        <div class="fact">
          <h2 class="fact-title"><span>Ein Team mit Haltung</span></h2>
          <p>Sie arbeiten in einem freundlichen, über Jahre gewachsenen Team mit hoher personeller Kontinuität und geringer Fluktuation.</p>
        </div>
        <div class="fact">
          <h2 class="fact-title"><span>Zeit für gute Medizin</span></h2>
          <p>Unsere Patientinnen und Patienten sind überwiegend gut bis sehr gut situiert, wertschätzend und therapieoffen. Das ermöglicht ruhiges, strukturiertes Arbeiten mit Fokus auf Qualität, Beziehung und nachhaltige Behandlung.</p>
        </div>
      </div>
      <div class="fact wide">
        <h2 class="fact-title"><span>Und sonst?</span></h2>
        <p>Der Praxisalltag ist klar strukturiert, ruhig und verlässlich. Geregelte und in Abstimmung flexible Arbeitszeiten ohne Wochenend- oder Nachtdienste, eine sehr gute leistungsbezogene Vergütung sowie ein respektvoller, wertschätzender Umgang auf Augenhöhe schaffen ein Umfeld, in dem man sich auf die medizinische Arbeit konzentrieren und langfristig wohlfühlen kann.</p>
      </div>
    </section>

    <footer class="contact">
      <div class="contact-note">
        <p>Wir freuen uns über eine unkomplizierte Kontaktaufnahme per<br><strong>E-Mail oder Telefon</strong> – gerne auch ganz unverbindlich und ohne vollständige Bewerbungsunterlagen.</p>
        <p class="contact-mail"><span class="label">E-Mail:</span> Melina.Korvath@praxis-lindenhof.ch</p>
      </div>
      <address class="contact-address">
        <div class="org">Praxis Lindenhof</div>
        <div>Mühlegasse 7</div>
        <div>4718 Erlenbrunn</div>
        <div><span class="label">Tel:</span> 062 555 01 23</div>
      </address>
    </footer>
  </article>
</body>
</html>
```